Modern Label for Loose Tea pouches on 4.5x6 Label

We need a new label for our teas that is very simple in design, but stylish and modern. This will be used to print labels for our loose tea pouches. The label will be at max 4.5x6 inches in size. There should be a place for the tea name, description, ingredients, and size that is changeable.
Preferably an AI file that allows me to setup variables to change the above items. There will also need to be our logo which is supplied, and our address on the label.
Address:
Brevo Leaf
846 Lower Maple Lane
Highland, NY 12617
Target Market(s)
Tea Lovers
Requirements
Must have
- Adobe Illustrator file with variables setup for replacement of tea name, description, ingredients, and size (weights 2oz, 4oz, 8oz, 1lb)

```html
<!DOCTYPE html>
<html lang="en">
<head>
<meta charset="utf-8">
<title>Brevo Leaf – Premium Detox Tea Label</title>
<link href="https://fonts.googleapis.com/css2?family=Montserrat:ital,wght@0,400;0,500;0,600;0,700;1,400;1,700&family=Open+Sans:wght@400;700&display=swap" rel="stylesheet">
<style>
  :root {
    --backdrop: #ececec;
    --label: #ffffff;
    --pink: #e35fb3;
    --lime: #c6dd3c;
    --ink: #1e1e1e;
    --muted: #555555;
  }
  html, body {
    margin: 0;
    padding: 0;
    width: 1200px;
    height: 942px;
    overflow: hidden;
    background: var(--backdrop);
  }
  .canvas {
    position: relative;
    width: 1200px;
    height: 942px;
  }
  .label {
    position: absolute;
    left: 345px;
    top: 90px;
    width: 510px;
    height: 760px;
    background: var(--label);
    box-shadow: 0 2px 10px rgba(0,0,0,0.08);
  }
  .brand-mark {
    position: absolute;
    left: 50%;
    top: 100px;
    width: 52px;
    height: 52px;
    margin-left: -26px;
    border-radius: 50%;
    background: var(--pink);
  }
  .brand-name {
    position: absolute;
    left: 0;
    right: 0;
    top: 190px;
    margin: 0;
    text-align: center;
    font-family: "Montserrat", sans-serif;
    font-weight: 600;
    font-size: 32px;
    letter-spacing: 1px;
    color: var(--lime);
  }
  .leaf-ornament {
    position: absolute;
    left: 50%;
    width: 92px;
    height: 46px;
    margin-left: -46px;
    background: var(--lime);
  }
  .leaf-ornament--top { top: 302px; border-radius: 46px 46px 8px 8px; }
  .leaf-ornament--bottom { top: 452px; border-radius: 8px 8px 46px 46px; }
  .tea-grade {
    position: absolute;
    left: 0; right: 0;
    top: 360px;
    margin: 0;
    text-align: center;
    font-family: "Montserrat", sans-serif;
    font-weight: 600;
    font-size: 18px;
    letter-spacing: 3.5px;
    color: var(--pink);
  }
  .tea-name {
    position: absolute;
    left: 0; right: 0;
    top: 384px;
    margin: 0;
    text-align: center;
    font-family: "Montserrat", sans-serif;
    font-weight: 500;
    font-size: 58px;
    line-height: 70px;
    color: var(--pink);
  }
  .tea-description {
    position: absolute;
    left: 82px;
    width: 346px;
    top: 538px;
    margin: 0;
    text-align: center;
    font-family: "Montserrat", sans-serif;
    font-style: italic;
    font-size: 10.6px;
    line-height: 15.5px;
    color: var(--ink);
  }
  .tea-description strong { font-weight: 700; }
  .net-weight {
    position: absolute;
    left: 0; right: 0;
    top: 640px;
    margin: 0;
    text-align: center;
    font-family: "Open Sans", sans-serif;
    font-size: 13px;
    color: var(--ink);
  }
  .net-weight strong { font-weight: 700; }
  .tea-ingredients {
    position: absolute;
    left: 82px;
    width: 346px;
    top: 668px;
    margin: 0;
    text-align: center;
    font-family: "Montserrat", sans-serif;
    font-size: 10px;
    line-height: 14px;
    color: var(--ink);
  }
  .tea-ingredients strong { font-weight: 700; }
  .company-address {
    position: absolute;
    left: 0; right: 0;
    top: 700px;
    margin: 0;
    text-align: center;
    font-family: "Montserrat", sans-serif;
    font-style: normal;
    font-size: 9.5px;
    line-height: 13px;
    color: var(--muted);
  }
</style>
</head>
<body>
  <main class="canvas">
    <section class="label">
      <div class="brand-mark"></div>
      <h2 class="brand-name">BREVO LEAF</h2>

      <div class="leaf-ornament leaf-ornament--top" role="img" aria-label="Decorative green leaf sprig ornament"></div>
      <p class="tea-grade">PREMIUM</p>
      <h1 class="tea-name">DETOX TEA</h1>
      <div class="leaf-ornament leaf-ornament--bottom" role="img" aria-label="Decorative green leaf sprig ornament"></div>

      <p class="tea-description"><strong>Brevo Leaf</strong> is a great way to <strong>detoxify</strong> &amp; <strong>cleanse</strong> your <strong>body naturally</strong>. With using <strong>100% organic ingredients</strong> our Lorem ipsum dolor sit amet, consectetur adipisicing elit, <strong>sed do eiusmod tempor</strong> incididunt ut labore et dolore <strong>magna</strong> aliqua. Ut enim ad minim veniam, quis nostrud <strong>exercitation</strong>.</p>

      <p class="net-weight">NET Weight: <strong>2 oz</strong></p>

      <p class="tea-ingredients"><strong>Ingredients:</strong> green tea, lemongrass, ginger root, dandelion, peppermint.</p>

      <address class="company-address">Brevo Leaf<br>846 Lower Maple Lane<br>Highland, NY 12617</address>
    </section>
  </main>
</body>
</html>
```